Morvel & Morvel**

Ionic Vela-Mag (400 mg) 4 oz
Liquid Ionic B12 (1,000 mcg) 2 oz
Probiotic 55 Billion 30 CT
Liquid Potassium 99mg
Liquid Iodide 225mcg
Liquid Strontium 100 mg
Liquid Iron 22mg
Liquid Ionic Zinc (50 mg) 2 oz
Liquid Ionic Selenium (300 mcg) 2 oz
Lonic Boron 6 mg
Fulvic Acid 250 mg
Chromium 550 mcg
Ox Bile 500 mg
Vitamin D3 1000 IU
Liver Support 1000 IU
Tonify blood 1000 IU
Adrenal Support 1000 IU
Constipation 1000 IU

Target Market(s)

public

Industry/Entity Type

Health And Wellness

Font styles to use
Serif

Requirements
Must have
• color
Nice to have
• I would like to see the designer's views.
Should not have
• I don't have any

```html
<!DOCTYPE html>
<html lang="en">
<head>
<meta charset="utf-8">
<title>Morvel &amp; Morvel – Ionic Vela-Mag Label</title>
<link rel="stylesheet" href="https://fonts.googleapis.com/css2?family=Crimson+Pro:wght@400;600;700&display=swap">
<style>
  :root {
    --canvas-bg: #e1e2de;
    --label-white: #f4f4f5;
    --navy-deep: #1f2468;
    --navy-bright: #3d419c;
    --brand-accent: #8e2a4a;
    --silver: #b9bcc4;
    --text-white: #f7f7fa;
  }
  html, body {
    margin: 0;
    padding: 0;
    width: 1200px;
    height: 1200px;
    overflow: hidden;
    background: var(--canvas-bg);
  }
  .canvas {
    position: relative;
    width: 1200px;
    height: 1200px;
  }
  .product-label {
    position: absolute;
    left: 240px;
    top: 58px;
    width: 720px;
    height: 1084px;
    box-shadow: 0 6px 24px rgba(0,0,0,0.08);
  }
  .label-art text {
    font-family: "Crimson Pro", serif;
  }
  .brand-name { fill: var(--navy-deep); font-weight: 600; }
  .product-kind { fill: var(--text-white); font-weight: 400; }
  .product-name { fill: var(--text-white); font-weight: 600; }
  .product-strength { fill: var(--navy-deep); font-weight: 700; }
  .product-category { fill: var(--text-white); font-weight: 600; }
  .product-volume { fill: var(--navy-deep); font-weight: 700; }
</style>
</head>
<body>
<main class="canvas">
  <svg class="product-label label-art" viewBox="0 0 720 1084" xmlns="http://www.w3.org/2000/svg" aria-label="Morvel &amp; Morvel Ionic Vela-Mag 400 mg label">
    <defs>
      <linearGradient id="navyFill" x1="0" y1="0" x2="1" y2="0">
        <stop offset="0" stop-color="#1f2468"/>
        <stop offset="1" stop-color="#3d419c"/>
      </linearGradient>
    </defs>

    <rect class="label-base" x="0" y="0" width="720" height="1084" fill="var(--label-white)"/>

    <rect class="top-tab" x="196" y="0" width="328" height="30" fill="var(--navy-deep)"/>

    <circle class="brand-mark" cx="360" cy="150" r="72" fill="var(--brand-accent)"/>

    <text class="brand-name" x="360" y="318" font-size="62" text-anchor="middle">Morvel &amp; Morvel</text>

    <rect class="title-shadow" x="33" y="398" width="652" height="302" rx="16" fill="var(--silver)"/>
    <rect class="title-panel" x="29" y="390" width="652" height="300" rx="16" fill="url(#navyFill)"/>
    <text class="product-kind" x="360" y="490" font-size="72" text-anchor="middle">Ionic</text>
    <text class="product-name" x="356" y="640" font-size="140" text-anchor="middle" textLength="570" lengthAdjust="spacingAndGlyphs">Vela-Mag</text>

    <text class="product-strength" x="651" y="790" font-size="92" text-anchor="end">400 mg</text>

    <path class="wave-edge" d="M0 792 Q 330 930 720 858 L720 880 Q 330 952 0 814 Z" fill="var(--silver)"/>
    <path class="wave-band" d="M0 812 Q 330 950 720 878 L720 1084 L0 1084 Z" fill="url(#navyFill)"/>

    <text class="product-category" x="360" y="998" font-size="40" text-anchor="middle">Dietary Supplement</text>

    <rect class="volume-pill" x="234" y="1034" width="240" height="50" rx="6" fill="var(--label-white)"/>
    <text class="product-volume" x="354" y="1068" font-size="30" text-anchor="middle">4 oz (118 ml)</text>
  </svg>
</main>
</body>
</html>
```